Medical supplies company needs a catalogue re-design

Our present catalogue is spread over a number of pages but this needs to be reduced. 4-5 images would require to be on each page. It needs to be professional, simple and elegant. The photos and descriptors need to be adjacent to each other. It should be able to be emailed conventionally as an e-catalogue without it being compressed. an email with existing catalogue will be emailed to anyone interested.
https://www.filevarn.com/s/82kqtb5wzrmuyap/consumables%20photos%20and%20descriptions.pdf?dl=0
Target Market(s)
medical practices, hospitals
Industry/Entity Type
Medical Supply

```html
<!DOCTYPE html>
<html lang="en">
<head>
<meta charset="utf-8">
<title>Velora Care – 2018 Winter Catalogue</title>
<link href="https://fonts.googleapis.com/css2?family=Open+Sans:wght@300;400;600;700&display=swap" rel="stylesheet">
<style>
:root{
  --backdrop:#d6d6d6;
  --page:#ffffff;
  --column:#eef0f4;
  --navy:#1d3556;
  --heading-blue:#4a8ed1;
  --rule:#5e90c9;
  --divider:#b9cde3;
  --body:#3f4a57;
  --brand-red:#d9262b;
  --tile-blue:#5b8fcb;
  --tile-red:#d2665e;
  --tile-green:#98c15d;
}
*{margin:0;padding:0;box-sizing:border-box}
html,body{width:1200px;height:1122px;overflow:hidden;background:var(--backdrop)}
body{position:relative;font-family:"Open Sans",Arial,sans-serif;color:var(--body)}
.page{position:absolute;width:382px;height:541px;background:var(--page);overflow:hidden}
.p1{left:13px;top:14px}.p2{left:409px;top:14px}.p3{left:805px;top:14px}
.p4{left:13px;top:569px}.p5{left:409px;top:569px}.p6{left:805px;top:569px}
.column{position:absolute;top:0;bottom:0;background:var(--column)}
.abs{position:absolute}
.section-title{position:absolute;left:18px;top:16px;font-size:24px;font-weight:700;color:var(--navy);letter-spacing:.2px}
.section-rule{position:absolute;left:18px;width:348px;top:47px;height:2px;background:var(--rule)}
.divider{position:absolute;left:18px;width:348px;height:1px;background:var(--divider)}
.photo{position:absolute;border-radius:1px}
.info{position:absolute;font-size:7px;line-height:1.5}
.info h3{font-size:11.5px;font-weight:700;color:var(--navy);line-height:1.25;margin-bottom:3px}
.info h4{font-size:10px;font-weight:700;color:var(--heading-blue);line-height:1.2;margin-bottom:2px}
.info .sub{font-size:7.5px;font-weight:600;color:var(--heading-blue);margin:-2px 0 3px}
.info ul{list-style:none}
.info li{padding-left:6px;text-indent:-6px;margin-bottom:3px}
.info li::before{content:"• "}
.info p{margin-bottom:3px}
.tight li{margin-bottom:1.5px}
.tight p{margin-bottom:1.5px}
/* cover */
.cover-photo{position:absolute;left:37px;top:37px;width:310px;height:157px;background:linear-gradient(180deg,#8a7f5d 0%,#a8a488 45%,#d9d8cf 80%,#fff 100%)}
.brand{position:absolute;left:136px;top:68px;font-size:22px;font-weight:700;color:var(--brand-red);letter-spacing:1px}
.cover-title{position:absolute;left:37px;top:270px;width:310px;text-align:right;font-size:29px;color:var(--brand-red);white-space:nowrap}
.cover-title .year{font-weight:300}
.cover-title .name{font-weight:700}
.tile{position:absolute;top:385px;width:102px;height:101px;color:#fff;font-weight:700;font-size:11px;line-height:1.3;padding:5px 6px}
.cover-rule{position:absolute;left:37px;width:309px;top:505px;height:2px;background:var(--rule)}
.intro{position:absolute;left:18px;top:36px;width:348px;font-size:7px;line-height:1.55}
.intro h2{font-size:11.5px;font-weight:700;color:var(--navy);text-align:center;margin:-16px 0 6px}
.intro p{margin-bottom:4px}
.cols{display:flex;gap:12px;font-size:5.5px;line-height:1.4}
</style>
</head>
<body>

<!-- Cover -->
<section class="page p1">
  <div class="cover-photo" role="img" aria-label="Smiling older adults walking outdoors, one with a walking frame and one in a wheelchair"></div>
  <div class="brand">VELORA CARE</div>
  <h1 class="cover-title"><span class="year">2018 </span><span class="name">Winter Catalogue</span></h1>
  <div class="tile" style="left:37px;background:var(--tile-blue)">MEDICAL<br>CONSUMABLES</div>
  <div class="tile" style="left:140px;background:var(--tile-red)">MOBILITY<br>EQUIPMENT</div>
  <div class="tile" style="left:244px;background:var(--tile-green)">CONSUMER<br>HEALTH</div>
  <div class="cover-rule"></div>
</section>

<!-- Wound Care -->
<section class="page p2">
  <div class="column" style="left:27px;width:121px;top:49px"></div>
  <h2 class="section-title">Wound Care</h2>
  <div class="section-rule"></div>
  <div class="photo" style="left:39px;top:66px;width:97px;height:84px;background:radial-gradient(circle at 45% 50%,#fff 0 35%,#9fc0e0 70%,#3f78b8)" role="img" aria-label="Roll of white nonwoven tape"></div>
  <div class="info" style="left:157px;top:80px;width:205px">
    <h3>High Quality Nonwoven Tape</h3>
    <ul><li>Non-allergenic and suitable for the most sensitive and soft skin.</li><li>Box of 10</li></ul>
  </div>
  <div class="divider" style="top:169px"></div>
  <div class="photo" style="left:39px;top:188px;width:97px;height:71px;background:linear-gradient(135deg,#1f4fa8,#e9edf5 50%,#2b5fb8)" role="img" aria-label="Packets of wound closure strips on a blue background"></div>
  <div class="info" style="left:157px;top:186px;width:205px">
    <h3>Wound Closure Strips</h3>
    <ul><li>Reinforced strips of microporous material for fast and effective wound closure or to be applied to wounds that have been stitched to provide extra tensile support.</li><li>3mm by 75mm (five pcs per package, 50 packages in a box)</li><li>6mm by 75mm (three pcs per package, 50 packages in a box)</li></ul>
  </div>
  <div class="divider" style="top:308px"></div>
  <div class="photo" style="left:39px;top:332px;width:97px;height:106px;background:linear-gradient(180deg,#f3f5f2,#e2e6e0 60%,#e7cdb3 75%,#f1f2f0)" role="img" aria-label="Film island dressing with gauze pad and its sterile pouch"></div>
  <div class="info" style="left:157px;top:325px;width:205px">
    <h3>Film Island Dressing with Pad</h3>
    <ul><li>Waterproof dressings with a pad to absorb wound exudate. These are used following surgical procedures to cover wounds to prevent infection.</li></ul>
    <p>1.) Made of transparent PU film with gauze pad in the centre, 2.) Acts as a barrier to bacteria, debris and water, 3.) 50 pcs per box</p>
    <ul><li>3mm by 75mm (five pcs per package, 50 packages in a box)</li><li>6mm by 75mm (three pcs per package, 50 packages in a box)</li></ul>
  </div>
</section>

<!-- Film island / bandages -->
<section class="page p3">
  <div class="column" style="left:148px;width:234px;top:106px"></div>
  <div class="intro">
    <h2>Film Island Dressing Without Pad</h2>
    <p>These dressings are waterproof, and sterile. They allow the wound to breathe and are used for minor wounds. Can also be used with sterile gauze for minor wounds and burns.</p>
    <p>1. Made of transparent PU film 2. Keeps wound dry and protects against water, dirt and bacteria 3. 50 per box</p>
    <p>Sizes: 4.4cm by 4.4cm and 6cm by 7cm</p>
  </div>
  <div class="divider" style="top:106px"></div>
  <div class="photo" style="left:37px;top:114px;width:102px;height:98px;background:linear-gradient(90deg,#c99d8a,#e6c4b3 50%,#c7937f)" role="img" aria-label="Rolls of skin-tone elastic bandage"></div>
  <div class="info tight" style="left:157px;top:115px;width:205px">
    <h4>Wound Closure Strips</h4><div class="sub">Bandages (7.5 cm x 4.5 m, 10cm x 4.5 m)</div>
    <ul><li>Ideal for treatment, after-care &amp; prevention of sports injuries</li><li>Secured with lightweight metal clips</li><li>knit design offers strength, comfort &amp; breathability</li><li>Individually wrapped</li></ul><p>(12 rolls per box)</p>
  </div>
  <div class="divider" style="top:221px"></div>
  <div class="photo" style="left:37px;top:230px;width:102px;height:74px;background:linear-gradient(90deg,#ddd5c2,#f1ece0 50%,#d8cfbb)" role="img" aria-label="Rolls of unbleached crepe bandage"></div>
  <div class="info tight" style="left:157px;top:235px;width:205px">
    <h4>Unbleached Crepe Elastic</h4><div class="sub">Bandages (7.5 cm x 4.5 m, 10cm x 4.5 m)</div>
    <ul><li>Ideal for holding dressings in place</li><li>Can be used for strapping</li></ul><p>(12 rolls per box)</p>
  </div>
  <div class="divider" style="top:313px"></div>
  <div class="photo" style="left:37px;top:324px;width:102px;height:80px;background:radial-gradient(circle at 80% 50%,#f4f4f4 0 14%,#e2353e 30%,#c9242c)" role="img" aria-label="Roll of red cohesive bandage"></div>
  <div class="info tight" style="left:157px;top:322px;width:205px">
    <h4>Cohesive Bandages</h4><div class="sub">(7.5 cm x 4.5 m, 10cm x 4.5 m)</div>
    <ul><li>Offers compression to support a joint or muscle</li><li>Secures wound dressings &amp; is painless when removed</li><li>Secures to itself &amp; can be torn by hand</li><li>Won't leave any sticky residue</li><li>Conforms to all body contours</li></ul>
  </div>
  <div class="divider" style="top:418px"></div>
  <div class="photo" style="left:37px;top:432px;width:102px;height:62px;background:linear-gradient(160deg,#f5f6f8,#cfe0f0 50%,#f0c3c3 80%,#f6f6f6)" role="img" aria-label="Boxes of zinc oxide plaster with plastic tins"></div>
  <div class="info tight" style="left:157px;top:426px;width:205px">
    <h4>Transparent Plaster With Plastic Tin</h4>
    <ul><li>Zinc oxide tape used for securing dresses, particularly along joints and contoured body parts.</li><li>Comfortable and breathable</li><li>Strong adhesion</li></ul><p>2.5cm by 9m (12 per box)</p>
  </div>
</section>

<!-- Dressings -->
<section class="page p4">
  <div class="column" style="left:0;width:130px"></div>
  <div class="photo" style="left:40px;top:16px;width:77px;height:128px;background:linear-gradient(180deg,#eef1f7,#fafafa 55%,#e9e9e9)" role="img" aria-label="Non woven adhesive wound dressing and packet"></div>
  <div class="info tight" style="left:139px;top:18px;width:235px">
    <h4>Non Woven Adhesive Wound Dressing</h4>
    <ul><li>Convenient all in one sterile dressing that can be used for a large range of wound and skin lesions.</li><li>It is well absorbent and non adherent to wounds with minimal risk of skin reactions.</li><li>It protects open wounds and reduces wound infection</li><li>Not waterproof</li><li>Used for both surgical wound care and post traumatic wound closure</li></ul>
    <p>50 pcs per box (6cm by 8cm), 100 pcs per box (10cm by 10cm)</p><p>Sizes: 6cm by 8cm, 10cm by 10cm</p>
  </div>
  <div class="divider" style="top:151px"></div>
  <div class="photo" style="left:40px;top:158px;width:77px;height:114px;background:linear-gradient(180deg,#f3f4f6,#f7f7f7 50%,#eed9b8 70%,#f6f6f6)" role="img" aria-label="Extra thin hydrocolloid dressing and packet"></div>
  <div class="info tight" style="left:139px;top:158px;width:235px">
    <h4>Hydrocolloid Dressing (extra thin)</h4>
    <ul><li>This is for low or moderate exudate wounds. Suitable for venous ulcers, bed sores, superficial burns, post operative wounds and healing of chronic ulcers.</li><li>Provides a waterproof barrier over the dressing.</li><li>Does not damage newly formed tissues on removal</li><li>Can be cut to fit</li><li>Needs to be changed every two to three days</li></ul>
    <p>7.5cm by 7.5cm (25 pcs per box) and 10cm by 10cm<br>(10 pcs per box)</p>
  </div>
  <div class="divider" style="top:279px"></div>
  <div class="photo" style="left:40px;top:284px;width:77px;height:120px;background:linear-gradient(180deg,#f3f4f6,#f6f6f6 50%,#e8c98f 70%,#f3f3f3)" role="img" aria-label="Hydrocolloid dressing with thin border and packet"></div>
  <div class="info tight" style="left:139px;top:286px;width:235px">
    <h4>Hydrocolloid Dressing (with thin border)</h4>
    <ul><li>Used for light to moderate exuding wounds.</li><li>Suitable for venous ulcers, bed sores, superficial burns, post operative wounds and healing of chronic ulcers.</li><li>Contains hydrocolloid dressing with thin border which facilitates the adherence of the hydrocolloid dressing to the wound</li><li>On removal, does not damage the newly formed healing tissue.</li><li>Change of dressing every two to three days</li></ul>
    <p>7.5cm by 7.5cm (25 pcs per box) and 10cm by 10cm<br>(10 pcs per box)</p>
  </div>
  <div class="divider" style="top:407px"></div>
  <div class="photo" style="left:40px;top:412px;width:77px;height:120px;background:linear-gradient(180deg,#f4f4f5,#f7f7f7 45%,#dcc2a4 65%,#f1f1f1)" role="img" aria-label="Self adhesive silicone foam dressing and packet"></div>
  <div class="info tight" style="left:139px;top:414px;width:235px">
    <h4>Silicone Foam Dressing (Self Adhesive)</h4>
    <p>Suitable for low to high exudative wounds</p><p>Can be used for all stages of wound healing</p><p>Can be used for:</p>
    <div class="cols"><div>• First to third degree burns<br>• Skin graft donor and recipient sites<br>• Ulcers, pressure sores and cavity wounds</div><div>• Post surgical wounds<br>• Infected wounds with copious exudate</div></div>
    <p style="margin-top:3px">The foam dressing absorbs excess exudate and offers a water-proof bacteria resistant environment.</p>
    <p>10cm by 10cm (10 pcs per box)</p>
  </div>
</section>

<!-- Instruments -->
<section class="page p5">
  <div class="column" style="left:18px;width:130px;top:49px"></div>
  <h2 class="section-title">Instruments</h2>
  <div class="section-rule"></div>
  <div class="photo" style="left:42px;top:66px;width:93px;height:90px;background:linear-gradient(90deg,#f0f3f8,#dde7f3 50%,#e4ebf4)" role="img" aria-label="Sterile pouch containing surgical pack instruments"></div>
  <div class="info" style="left:157px;top:74px;width:205px">
    <h3>Disposable Surgical Pack</h3>
    <ul><li>Iris Scissors 11.5cm</li><li>Needle holder 12.5cm</li><li>Tooth forcep 12.7cm</li><li>Paper blister back 10x20cm</li></ul>
  </div>
  <div class="divider" style="top:162px"></div>
  <div class="photo" style="left:42px;top:177px;width:93px;height:93px;background:linear-gradient(90deg,#f0f3f8,#dde7f3 50%,#e4ebf4)" role="img" aria-label="Sterile pouch containing iris scissors"></div>
  <div class="info" style="left:157px;top:184px;width:205px">
    <h3>Iris Scissors 11.5cm</h3>
    <ul><li>Iris Scissors 11.5cm straight</li><li>Stainless Steel</li><li>Sterile</li><li>Paper blister back 10x20cm</li></ul>
  </div>
  <div class="divider" style="top:278px"></div>
  <div class="photo" style="left:42px;top:286px;width:93px;height:90px;background:linear-gradient(90deg,#f0f3f8,#dde7f3 50%,#e4ebf4)" role="img" aria-label="Sterile pouch containing mosquito forceps"></div>
  <div class="info" style="left:157px;top:290px;width:205px">
    <h3>Halstead Mosquito Forceps Straight 14cm</h3>
    <ul><li>Halstead Mosquito Forcep</li><li>14cm Straight</li><li>Stainless Steel</li><li>Sterile</li></ul>
  </div>
  <div class="divider" style="top:389px"></div>
  <div class="photo" style="left:42px;top:397px;width:93px;height:105px;background:linear-gradient(90deg,#f0f3f8,#dde7f3 50%,#e4ebf4)" role="img" aria-label="Sterile pouch containing tooth forceps"></div>
  <div class="info" style="left:157px;top:406px;width:205px">
    <h3>Tooth Forceps, Dressing<br>and Tissue, Adson 12.5cm</h3>
    <ul><li>Tooth Forceps, Dressing and Tissue, Adson 12.5cm</li><li>Straight</li><li>Stainless Steel</li><li>Sterile</li></ul>
  </div>
</section>

<!-- Instruments continued -->
<section class="page p6">
  <div class="column" style="left:27px;width:121px"></div>
  <div class="photo" style="left:40px;top:36px;width:94px;height:100px;background:linear-gradient(90deg,#f0f3f8,#dde7f3 50%,#e4ebf4)" role="img" aria-label="Sterile pouch containing splinter forceps"></div>
  <div class="info" style="left:157px;top:58px;width:205px">
    <h3>Splinter Forceps; Hunter 11.5cm</h3>
    <ul><li>Splinter Forceps; Hunter 11.5cm Straight</li><li>Stainless Steel</li><li>Sterile</li></ul>
  </div>
  <div class="divider" style="top:154px"></div>
  <div class="photo" style="left:40px;top:172px;width:94px;height:108px;background:linear-gradient(90deg,#f0f3f8,#dde7f3 50%,#e4ebf4)" role="img" aria-label="Sterile pouch containing dressing forceps"></div>
  <div class="info" style="left:157px;top:186px;width:205px">
    <h3>Forcep dressing fine 12.5cm</h3>
    <ul><li>Forcep dressing fine 12.5cm</li><li>Straight</li><li>Stainless Steel</li><li>Sterile</li></ul>
  </div>
  <div class="divider" style="top:290px"></div>
  <div class="photo" style="left:40px;top:307px;width:94px;height:99px;background:linear-gradient(90deg,#f0f3f8,#dde7f3 50%,#e4ebf4)" role="img" aria-label="Sterile pouch containing sharp scissors"></div>
  <div class="info" style="left:157px;top:320px;width:205px">
    <h3>Sharp Scissors 12.5cm</h3>
    <ul><li>Sharp Scissors 12.5cm</li><li>Straight</li><li>Stainless Steel</li><li>Sterile</li></ul>
  </div>
</section>

</body>
</html>
```